Startup Drone Platform Company business card

We are needing a business card design for our employees. We are a startup drone platform. We are looking for a business card that has our logo on one side, with the employee/company details on the opposite side. We are looking for something that is very eye catching, modern, and bold.

Target Market(s)

This will target both drone pilots and drone businesses, along with all the industries that could utilize drone services (aerial video, aerial photos, inspections, 3d mapping, etc).

Industry/Entity Type

Business

```html
<!DOCTYPE html>
<html lang="en">
<head>
<meta charset="utf-8">
<title>Skylane Aerial – Business Card</title>
<link href="https://fonts.googleapis.com/css2?family=Questrial&display=swap" rel="stylesheet">
<style>
  :root {
    --backdrop: #3a3a3a;
    --card-white: #f7f7f7;
    --teal: #3bb5c1;
    --ink: #1e1e1e;
    --ink-soft: #4a4a4a;
    --rule: #c9c9c9;
    --white: #ffffff;
  }
  * { margin: 0; padding: 0; box-sizing: border-box; }
  html, body { width: 1200px; height: 750px; overflow: hidden; }
  body {
    background: var(--backdrop);
    font-family: "Questrial", sans-serif;
    position: relative;
  }
  .card {
    position: absolute;
    top: 228px;
    width: 462px;
    height: 262px;
    overflow: hidden;
  }
  .card-front { left: 124px; background: var(--card-white); }
  .card-back { left: 618px; background: var(--teal); }

  /* Front */
  .brand-block {
    position: absolute;
    left: 38px;
    top: 44px;
    width: 184px;
    text-align: center;
  }
  .brand-mark {
    display: block;
    margin: 0 auto 18px;
  }
  .brand-name {
    color: var(--ink);
    font-size: 15px;
    letter-spacing: 7px;
    line-height: 1.35;
    padding-left: 7px;
  }
  .divider {
    position: absolute;
    left: 214px;
    top: 48px;
    width: 1px;
    height: 140px;
    background: var(--rule);
  }
  .contact {
    position: absolute;
    left: 236px;
    top: 46px;
    color: var(--ink-soft);
  }
  .person-name {
    color: var(--teal);
    font-size: 20px;
    line-height: 1.2;
  }
  .person-title {
    color: var(--ink);
    font-size: 14px;
    margin-bottom: 10px;
  }
  .address { font-size: 12px; line-height: 1.3; margin-bottom: 6px; }
  .contact-line {
    display: flex;
    align-items: center;
    gap: 7px;
    font-size: 12px;
    line-height: 18px;
  }
  .contact-line svg { width: 11px; height: 11px; flex: none; }
  .front-footer {
    position: absolute;
    left: 0; bottom: 0;
  }
  .footer-url {
    position: absolute;
    left: 0; right: 0;
    bottom: 4px;
    text-align: center;
    color: var(--white);
    font-size: 12px;
    letter-spacing: 2.5px;
  }

  /* Back */
  .back-brand {
    position: absolute;
    right: 34px;
    top: 172px;
    text-align: center;
    color: var(--white);
  }
  .back-brand-name {
    font-size: 19px;
    letter-spacing: 9px;
    padding-left: 9px;
    line-height: 1.3;
  }
  .back-url {
    font-size: 12.5px;
    letter-spacing: 2px;
    margin-top: 4px;
  }
</style>
</head>
<body>

<section class="card card-front" aria-label="Business card front">
  <div class="brand-block">
    <svg class="brand-mark" width="58" height="58" viewBox="0 0 58 58" aria-hidden="true">
      <circle cx="29" cy="29" r="26" fill="none" stroke="var(--teal)" stroke-width="3"/>
    </svg>
    <div class="brand-name">SKYLANE<br>AERIAL</div>
  </div>

  <div class="divider"></div>

  <div class="contact">
    <div class="person-name">Maya Lindqvist</div>
    <div class="person-title">CEO/Founder</div>
    <div class="address">214 Harbor View Road<br>Juneau, Alaska 99801</div>
    <div class="contact-line">
      <svg viewBox="0 0 12 12" aria-hidden="true"><path d="M2.5 1 L4.5 1 L5.3 3.5 L4 4.5 Q5 7 7.5 8 L8.5 6.7 L11 7.5 L11 9.5 Q10.5 11 9 11 Q1 10 1 2.5 Q1 1 2.5 1 Z" fill="var(--teal)"/></svg>
      <span>555 210 4817</span>
    </div>
    <div class="contact-line">
      <svg viewBox="0 0 12 12" aria-hidden="true"><rect x="2.5" y="0.5" width="7" height="11" rx="1.2" fill="none" stroke="var(--teal)" stroke-width="1.2"/><rect x="4.5" y="9" width="3" height="1" fill="var(--teal)"/></svg>
      <span>555 738 6092</span>
    </div>
    <div class="contact-line">
      <svg viewBox="0 0 12 12" aria-hidden="true"><rect x="0.5" y="2.5" width="11" height="7.5" fill="var(--teal)"/><path d="M0.5 2.5 L6 7 L11.5 2.5" fill="none" stroke="var(--white)" stroke-width="1"/></svg>
      <span>maya@skylaneaerial.com</span>
    </div>
  </div>

  <svg class="front-footer" width="462" height="40" viewBox="0 0 462 40" aria-hidden="true">
    <path d="M0 24 Q231 -10 462 24 L462 40 L0 40 Z" fill="var(--teal)"/>
    <path d="M0 24 Q231 -10 462 24" fill="none" stroke="var(--ink)" stroke-width="3"/>
  </svg>
  <div class="footer-url">www.skylaneaerial.com</div>
</section>

<section class="card card-back" aria-label="Business card back">
  <div class="back-brand">
    <div class="back-brand-name">SKYLANE<br>AERIAL</div>
    <div class="back-url">www.skylaneaerial.com</div>
  </div>
</section>

</body>
</html>
```